Holvern Incorporated

Holvern is a business that provides consulting, and manages and supplies trades persons in the construction and heavy industries sector. We build, do maintenance, install machinery, and can manage projects or jobs. Would like or prefer more clean, classic designs. Blacks/greys, but open to almost anything.

Target Market(s)

Industrial/Construction/Manufacturing

Industry/Entity Type

Construction Company

Contact Information for Business Card

Clean, business name on the front, possibly have the details on the back, but open to any ideas.

Logo Text

We currently do not have a slogan, open to ideas

Font styles to use
Serif
Sans Serif

Colors

Designer to choose colors to be used in the design.

Requirements
Should not have
• the oval is not my logo, was just an idea. please don't send 20 designs with the oval

```html
<!DOCTYPE html>
<html lang="en">
<head>
<meta charset="utf-8">
<title>Holvern Incorporated — Business Card</title>
<link href="https://fonts.googleapis.com/css2?family=Roboto+Slab:wght@700&family=Roboto+Condensed:wght@400;700&display=swap" rel="stylesheet">
<style>
  :root {
    --backdrop: #6f6f6f;
    --card-dark: #2b2b2d;
    --card-light: #ffffff;
    --ink-dark: #1f1f21;
    --ink-light: #ffffff;
    --ink-muted: #555558;
  }
  * { margin: 0; padding: 0; box-sizing: border-box; }
  html, body {
    width: 1200px;
    height: 1200px;
    overflow: hidden;
    background: var(--backdrop);
  }
  .canvas {
    position: relative;
    width: 1200px;
    height: 1200px;
  }
  .card {
    position: absolute;
    left: 250px;
    width: 700px;
    height: 400px;
    box-shadow: 0 10px 24px rgba(0,0,0,0.25);
  }
  .card--front {
    top: 150px;
    background: var(--card-dark);
    display: flex;
    align-items: center;
    justify-content: center;
  }
  .card--back {
    top: 630px;
    background: var(--card-light);
  }
  .brand-name {
    font-family: "Roboto Slab", serif;
    font-weight: 700;
    letter-spacing: -0.5px;
    white-space: nowrap;
  }
  .card--front .brand-name {
    font-size: 62px;
    color: var(--ink-light);
  }
  .card--back .brand-name {
    position: absolute;
    left: 60px;
    top: 170px;
    font-size: 38px;
    color: var(--ink-dark);
  }
  .card--back .rule {
    position: absolute;
    left: 60px;
    top: 158px;
    width: 418px;
    height: 2px;
    background: var(--ink-dark);
  }
  .contact {
    position: absolute;
    right: 60px;
    top: 60px;
    width: 230px;
    text-align: right;
    font-family: "Roboto Condensed", sans-serif;
    color: var(--ink-dark);
  }
  .contact__name {
    font-weight: 700;
    font-size: 28px;
    line-height: 1;
    letter-spacing: 0.5px;
  }
  .contact__role {
    font-size: 15px;
    letter-spacing: 1px;
    color: var(--ink-muted);
    margin-top: 4px;
    padding-bottom: 8px;
    border-bottom: 2px solid var(--ink-dark);
  }
  .contact__address {
    margin-top: 16px;
    font-size: 17px;
    line-height: 1.35;
  }
  .contact__lines {
    margin-top: 14px;
    font-size: 17px;
    line-height: 1.35;
  }
</style>
</head>
<body>
  <main class="canvas">
    <section class="card card--front" aria-label="Business card front">
      <span class="brand-name">Holvern Incorporated</span>
    </section>

    <section class="card card--back" aria-label="Business card back">
      <div class="rule"></div>
      <span class="brand-name">Holvern Incorporated</span>
      <div class="contact">
        <div class="contact__name">YOUR NAME</div>
        <div class="contact__role">JOB POSITION</div>
        <div class="contact__address">
          2364 First Address Line<br>
          Second Address Line,56324
        </div>
        <div class="contact__lines">
          +0 123 456 7899<br>
          lorem@ipsum.com<br>
          websitename.com
        </div>
      </div>
    </section>
  </main>
</body>
</html>
```